Saltbush Creek Glow needing a box to hold our gorgeous hand poured candles that look high end.

We need a packaging design that showcases our gorgeous candles.
Would like whole box in turquoise with a black band around bottom with a thin silver separating the two and also silver band around very top as per image attached.
Our feature color is turquoise, silver , white and black.
With the current logo like the font but want it bolder. Please do in black with 'glow' in silver or white. Can I also see 'Saltbush Cree'k in white with 'glow' in silver just too see which stands out more.
Would like the blue butterfly image to top right of the 'er' in Creek. Can play with the design around the picture but would like the same shape of butterfly. Could be solid or just outline image.
Saltbush Creek Glow will over time involve into selling of body care products, skincare, food, wood work will be used on alot of branding so if this can be kept in mind thank you.
Box measurements 10cm width, 13cm height, depth 10cm. Hope it makes sense.

Target Market(s)

Tourism travellers from overseas wanting to take home a gift from the area they have visited

Industry/Entity Type

Work

Font styles to use
Script

Requirements
Must have
• Turquoise box with black band around bottom with thin silver seperating black and turquoise and also around very top of box as per the box picture attached.
Logo with single butterfly to top right. Please do font bolder and do in black and an image in white with the word glow in white (if black font) with glow in silver just want to see
Nice to have
• A butterfly insignia...would like someone to design a different concept of a butterfly ie. half of bold then light or abstract just something outside of the box idea not like all the ones you can just download from websites please thank you.
Should not have
• Too busy

```html
<!DOCTYPE html>
<html lang="en">
<head>
<meta charset="utf-8">
<title>Saltbush Creek Glow – Candle Box</title>
<link rel="stylesheet" href="https://fonts.googleapis.com/css2?family=Great+Vibes&family=Marcellus&family=Crimson+Text&display=swap">
<style>
  :root {
    --page: #e4e4e4;
    --turquoise-light: #8fe6f2;
    --turquoise: #3fc6e0;
    --turquoise-deep: #22a9cc;
    --silver: #f2f3f4;
    --silver-edge: #c9ccce;
    --band-black: #080808;
    --ink: #111111;
    --fold: rgba(0, 80, 110, 0.35);
  }
  * { margin: 0; padding: 0; box-sizing: border-box; }
  html, body { width: 1200px; height: 960px; overflow: hidden; }
  body {
    background: var(--page);
    display: flex;
    align-items: center;
    justify-content: center;
  }
  .box-net { display: flex; align-items: flex-start; }
  .panel {
    position: relative;
    width: 420px;
    height: 546px;
    display: flex;
    flex-direction: column;
  }
  .panel + .panel { box-shadow: inset 1px 0 0 var(--fold); }
  .band-silver-top {
    flex: none;
    height: 14px;
    background: linear-gradient(var(--silver), var(--silver-edge));
  }
  .body-turquoise {
    flex: none;
    height: 422px;
    overflow: hidden;
    position: relative;
    background:
      radial-gradient(ellipse at 50% 100%, var(--turquoise-light) 0%, transparent 55%),
      linear-gradient(160deg, var(--turquoise-deep) 0%, var(--turquoise) 45%, var(--turquoise-light) 100%);
    color: var(--ink);
  }
  .band-silver-divider {
    flex: none;
    height: 9px;
    background: linear-gradient(var(--silver), var(--silver-edge));
  }
  .band-black { flex: none; height: 92px; background: var(--band-black); }
  .band-silver-bottom {
    flex: none;
    height: 9px;
    background: linear-gradient(var(--silver), var(--silver-edge));
  }

  .brand-name {
    font-family: "Great Vibes", cursive;
    color: var(--ink);
    font-weight: 400;
    line-height: 1.1;
    display: flex;
    align-items: center;
    justify-content: center;
    gap: 10px;
    white-space: nowrap;
  }
  .brand-mark {
    flex: none;
    width: 12px; height: 12px;
    border-radius: 50%;
    background: var(--ink);
    align-self: flex-start;
    margin-top: 4px;
  }

  /* Front panel */
  .front .brand-name { font-size: 50px; margin-top: 56px; }
  .front .headline {
    font-family: "Marcellus", serif;
    font-weight: 400;
    font-size: 31px;
    text-align: center;
    margin-top: 50px;
    letter-spacing: 0.5px;
  }
  .ornament-divider {
    display: block;
    margin: 20px auto 0;
    height: 16px;
    background: linear-gradient(90deg, transparent, rgba(17,17,17,0.55), transparent);
    border-radius: 8px;
  }
  .front .ornament-divider { width: 170px; }
  .front .intro {
    font-family: "Crimson Text", serif;
    font-size: 15px;
    line-height: 1.45;
    text-align: center;
    width: 300px;
    margin: 30px auto 0;
  }

  /* Side panel */
  .side .brand-name { font-size: 32px; margin-top: 40px; }
  .side .copy {
    font-family: "Crimson Text", serif;
    font-size: 11px;
    line-height: 1.48;
    text-align: justify;
    text-align-last: center;
    width: 330px;
    margin: 22px auto 0;
  }
  .side .ornament-divider { width: 150px; margin-top: 24px; }
</style>
</head>
<body>
  <main class="box-net">
    <section class="panel front">
      <div class="band-silver-top"></div>
      <div class="body-turquoise">
        <div class="brand-name">Saltbush Creek glow<span class="brand-mark"></span></div>
        <h1 class="headline">LOREM IPSUM DOLOR</h1>
        <div class="ornament-divider" role="img" aria-label="Decorative flourish divider"></div>
        <p class="intro">Lorem ipsum dolor sit amet, consectetur adipisicing elit, sed do eiusmod tempor incididunt ut labore et dolore magna aliqua.</p>
      </div>
      <div class="band-silver-divider"></div>
      <div class="band-black"></div>
      <div class="band-silver-bottom"></div>
    </section>

    <section class="panel side">
      <div class="band-silver-top"></div>
      <div class="body-turquoise">
        <div class="brand-name">Saltbush Creek glow<span class="brand-mark"></span></div>
        <p class="copy">Lorem ipsum dolor sit amet, consectetur adipisicing elit, sed do eiusmod tempor incididunt ut labore et dolore magna aliqua. Lorem ipsum dolor sit amet, consectetur adipisicing elit, sed do eiusmod tempor incididunt ut labore et dolore magna aliqua. Lorem ipsum dolor sit amet, consectetur adipisicing elit, sed do eiusmod tempor incididunt ut labore et dolore magna aliqua. Lorem ipsum dolor sit amet, consectetur adipisicing elit, sed do eiusmod tempor incididunt ut labore et dolore magna aliqua. Lorem ipsum dolor sit amet, consectetur adipisicing elit, sed do eiusmod tempor incididunt ut labore et dolore magna aliqua. Lorem ipsum dolor sit amet, consectetur adipisicing elit, sed do eiusmod tempor incididunt ut labore et dolore magna aliqua. Lorem ipsum dolor sit amet, consectetur adipisicing elit, sed do eiusmod tempor incididunt ut labore et dolore magna aliqua. Lorem ipsum dolor sit amet, consectetur adipisicing elit, sed do eiusmod tempor incididunt ut labore et dolore magna aliqua.</p>
        <div class="ornament-divider" role="img" aria-label="Decorative flourish divider"></div>
      </div>
      <div class="band-silver-divider"></div>
      <div class="band-black"></div>
      <div class="band-silver-bottom"></div>
    </section>
  </main>
</body>
</html>
```